" Somos uma escola de Yoga e oferecemos aulas, Cursos de Formaçao para Professores de Yoga, workshops e retiros de meditaçao pelo Brasil e em países como Costa Rica, Panamá, Bali e Tailandia. Trabalhamos com o metodo Yin e Yang.. onde yin é a energia da meditaçao, contemplaçao e observaçao e yang do movimento, rítmo, força e atividade. "

```html
<!DOCTYPE html>
<html lang="pt-BR">
<head>
<meta charset="utf-8">
<title>Serena Flow – Papel Timbrado</title>
<link href="https://fonts.googleapis.com/css2?family=Comfortaa:wght@400;700&display=swap" rel="stylesheet">
<style>
  :root {
    --backdrop: #e9e9e6;
    --paper: #ffffff;
    --green: #6cb33f;
    --green-dark: #4f9a2b;
    --ink: #4a4a4a;
    --mandala-tone: #eef3e8;
    --mandala-edge: #dfe8d5;
    --faint-name: #d6d6d6;
  }
  * { box-sizing: border-box; margin: 0; padding: 0; }
  html, body {
    width: 1200px;
    height: 1200px;
    overflow: hidden;
    background: var(--backdrop);
    font-family: "Comfortaa", sans-serif;
  }
  .letterhead {
    position: absolute;
    left: 300px;
    top: 160px;
    width: 600px;
    height: 880px;
    background: var(--paper);
    box-shadow: 0 6px 24px rgba(0,0,0,0.12);
    overflow: hidden;
  }
  .brand {
    position: absolute;
    top: 30px;
    left: 0;
    width: 100%;
    display: flex;
    flex-direction: column;
    align-items: center;
    gap: 8px;
  }
  .brand-dot {
    width: 34px;
    height: 34px;
    border-radius: 50%;
    background: var(--green);
  }
  .brand-name {
    font-size: 22px;
    font-weight: 700;
    color: var(--ink);
    letter-spacing: 0.5px;
  }
  .brand-tagline {
    font-size: 9px;
    font-weight: 700;
    color: var(--ink);
    letter-spacing: 4px;
  }
  .mandala {
    position: absolute;
    top: 150px;
    left: 50%;
    width: 520px;
    height: 520px;
    margin-left: -260px;
    border-radius: 50%;
    background: radial-gradient(circle, var(--paper) 0%, var(--paper) 62%, var(--mandala-tone) 70%, var(--mandala-edge) 84%, var(--paper) 100%);
    display: flex;
    align-items: center;
    justify-content: center;
  }
  .mandala-name {
    font-size: 48px;
    font-weight: 700;
    color: var(--faint-name);
  }
  .footer-wave {
    position: absolute;
    left: 0;
    bottom: 0;
    width: 600px;
    height: 130px;
  }
</style>
</head>
<body>
  <main class="letterhead">
    <header class="brand">
      <span class="brand-dot"></span>
      <span class="brand-name">serena flow</span>
      <span class="brand-tagline">YOGA SCHOOL</span>
    </header>

    <div class="mandala" role="img" aria-label="Faint circular mandala ornament in pale green behind the school name">
      <span class="mandala-name">serena flow</span>
    </div>

    <svg class="footer-wave" viewBox="0 0 600 130" preserveAspectRatio="none" aria-hidden="true">
      <defs>
        <linearGradient id="waveGreen" x1="0" y1="0" x2="0" y2="1">
          <stop offset="0" stop-color="var(--green)"/>
          <stop offset="1" stop-color="var(--green-dark)"/>
        </linearGradient>
      </defs>
      <path d="M0 60 C150 20 300 10 600 30" fill="none" stroke="var(--green)" stroke-width="3"/>
      <path d="M0 78 C160 36 320 26 600 46 L600 130 L0 130 Z" fill="url(#waveGreen)"/>
    </svg>
  </main>
</body>
</html>
```